Modern Banner and Window Decal Design For Law Firm Lawyer

We are looking for three modern and sophisticated banner design and window decal for our law firm.

Banner measurements/types:

1) Height: 130 cm Width: 160 cm (Outdoor banner)
2) Height: 200 cm Width: 85 cm (Pull up/retractable indoor banner)

Window Decal:
3) Height: 70cm width 70cm

Our law firm is based in Melbourne, Australia and we deal with property law mostly.

We prefer a white background with classic text in black or grey. We would also like a dash of colour so please use a green, blue or aqua colour palette that is consistent with our logo. Vector attached. A nice photo of property, Melbourne city viee, or family home would be nice.

We do not want any law related images - scales of justice, gavel or the like.

Our ultimate goal is to communicate that the firm is modern, professional and knowledgeable

We would like the following:

1. Our logo
2. Our services: - Property Law - Wills - Powers of Attorney - Probate - Estate Administration - Consultancy & Agency
3. Phone number
4. Web Address

5. For pull up/retractable banner we would also like the following text:

We use the latest digital technology and fixed-fees to provide fast and affordable legal advice that is easy to understand.

For privacy reasons, we will provide business details once we have decided on the winner.

We will monitor entries closely and promise to provide feedback and guidance on each entry.

Thank you very much for considering this project.

Target Market(s)

General public, professionals, lawyers and conveyancers

Industry/Entity Type

Law Firm

Font styles to use
Sans Serif

Colors
0393ce
34a6d7
0456a4
3176b5
acd037
33b8a4
86cfc6
00a990
9ccb3b

Requirements
Must have
• 1. Our logo
• 2. Our services: - Property Law - Wills - Powers of Attorney - Probate & Estate Administration - Consultancy & Agency
• 3. Phone number
• 4. Web Address
Nice to have
• Picture of Melbourne, Australia city ; property/buildings/lawyers
Should not have
• We do not want any law related images - scales of justice, gavel or the like.

```html
<!DOCTYPE html>
<html lang="en">
<head>
<meta charset="utf-8">
<title>Ridgeview Lawyers – Banners and Window Decal</title>
<link rel="stylesheet" href="https://fonts.googleapis.com/css2?family=Mulish:wght@400;600;700&display=swap">
<style>
  :root {
    --page-bg: #e6e8eb;
    --sheet: #ffffff;
    --ink-grey: #55575a;
    --brand-blue: #2ea3d8;
    --photo-light: #8fbdd6;
    --photo-mid: #4f8fb0;
    --photo-dark: #2c6a8a;
    --stand-light: #d5d8dc;
    --stand-dark: #a7abb1;
    --shadow: 0 6px 18px rgba(40, 50, 60, 0.18);
  }
  * { box-sizing: border-box; margin: 0; padding: 0; }
  html, body {
    width: 1200px; height: 1200px; overflow: hidden;
    background: var(--page-bg);
    font-family: "Mulish", "Helvetica Neue", Arial, sans-serif;
    color: var(--ink-grey);
  }
  .canvas { position: relative; width: 1200px; height: 1200px; }

  .piece {
    position: absolute;
    background: var(--sheet);
    box-shadow: var(--shadow);
    display: flex; flex-direction: column; align-items: center;
    overflow: hidden;
    text-align: center;
  }

  .brand {
    display: flex; align-items: center; gap: 0.5em;
    font-weight: 600; letter-spacing: 0.06em; line-height: 1.1;
    color: var(--ink-grey); text-transform: uppercase; text-align: left;
  }
  .brand-dot {
    width: 1.6em; height: 1.6em; border-radius: 50%;
    background: var(--brand-blue); flex: none;
  }

  .services { font-weight: 600; text-transform: uppercase; line-height: 1.55; white-space: nowrap; }
  .services .sep { color: var(--brand-blue); margin: 0 0.4em; }

  .contact { color: var(--brand-blue); font-weight: 700; white-space: nowrap; }

  .city-photo {
    margin-top: auto; width: 100%; flex: none;
    background: linear-gradient(180deg, var(--photo-light) 0%, var(--photo-mid) 50%, var(--photo-dark) 100%);
  }

  /* Window decal 70 x 70 */
  .decal { left: 60px; top: 50px; width: 500px; height: 500px; padding-top: 44px; }
  .decal .brand { font-size: 26px; margin-bottom: 28px; }
  .decal .services { font-size: 14px; }
  .decal .contact { font-size: 16px; margin-top: 18px; display: flex; gap: 28px; }
  .decal .city-photo { height: 180px; }

  /* Outdoor banner 160 x 130 */
  .outdoor { left: 40px; top: 610px; width: 560px; height: 455px; padding-top: 34px; }
  .outdoor .brand { font-size: 30px; margin-bottom: 22px; }
  .outdoor .services { font-size: 18px; }
  .outdoor .contact { font-size: 21px; margin-top: 12px; display: flex; gap: 44px; }
  .outdoor .city-photo { height: 150px; }

  /* Pull-up banner 85 x 200 */
  .pullup { left: 720px; top: 90px; width: 400px; height: 970px; padding-top: 44px; }
  .pullup .brand { font-size: 28px; margin-bottom: 34px; }
  .pullup .services { font-size: 22px; line-height: 1.2; list-style: none; }
  .pullup .services .dot {
    display: block; width: 8px; height: 8px; border-radius: 50%;
    background: var(--brand-blue); margin: 9px auto;
  }
  .pullup .contact { margin-top: 28px; line-height: 1.55; }
  .pullup .phone { font-size: 28px; }
  .pullup .web { font-size: 25px; }
  .pullup .intro {
    margin-top: 22px; padding: 0 20px;
    text-align: left; font-size: 17px; line-height: 1.4; letter-spacing: 0.03em;
  }
  .pullup .city-photo { height: 230px; }

  .stand {
    position: absolute; left: 708px; top: 1060px; width: 424px; height: 40px;
    background: linear-gradient(180deg, var(--stand-light), var(--stand-dark));
    border-radius: 6px;
  }
</style>
</head>
<body>
<main class="canvas">

  <section class="piece decal" aria-label="Window decal">
    <div class="brand"><span class="brand-dot"></span><span>Ridgeview<br>Lawyers</span></div>
    <div class="services">
      <div>Property Law<span class="sep">•</span>Wills</div>
      <div>Powers of Attorney<span class="sep">•</span>Probate</div>
      <div>Estate Administration<span class="sep">•</span>Consultancy &amp; Agency</div>
    </div>
    <div class="contact"><span>03 9000 4821</span><span>ridgeviewlawyers.com.au</span></div>
    <div class="city-photo" role="img" aria-label="Photo placeholder: blue-toned Melbourne city skyline"></div>
  </section>

  <section class="piece outdoor" aria-label="Outdoor banner">
    <div class="brand"><span class="brand-dot"></span><span>Ridgeview<br>Lawyers</span></div>
    <div class="services">
      <div>Property Law<span class="sep">•</span>Wills</div>
      <div>Powers of Attorney<span class="sep">•</span>Probate</div>
      <div>Estate Administration<span class="sep">•</span>Consultancy &amp; Agency</div>
    </div>
    <div class="contact"><span>03 9000 4821</span><span>ridgeviewlawyers.com.au</span></div>
    <div class="city-photo" role="img" aria-label="Photo placeholder: blue-toned Melbourne city skyline"></div>
  </section>

  <section class="piece pullup" aria-label="Pull-up banner">
    <div class="brand"><span class="brand-dot"></span><span>Ridgeview<br>Lawyers</span></div>
    <ul class="services">
      <li>Property Law</li><li><span class="dot"></span></li>
      <li>Wills</li><li><span class="dot"></span></li>
      <li>Powers of Attorney</li><li><span class="dot"></span></li>
      <li>Probate</li><li><span class="dot"></span></li>
      <li>Estate Administration</li><li><span class="dot"></span></li>
      <li>Consultancy &amp; Agency</li>
    </ul>
    <div class="contact">
      <div class="phone">03 9000 4821</div>
      <div class="web">ridgeviewlawyers.com.au</div>
    </div>
    <p class="intro">We use the latest digital technology and fixed-fees to provide fast and affordable legal advice that is easy to understand.</p>
    <div class="city-photo" role="img" aria-label="Photo placeholder: blue-toned Melbourne skyline above a river bridge"></div>
  </section>
  <div class="stand" aria-hidden="true"></div>

</main>
</body>
</html>
```